Splash Page Design For Thailands "Whatever Brings Joy" App

We are creating an app that will allow a tourist to request a variety of services on demand. Such as motorbike rentals, in room massage, pick up and laundry delivery service, maid cleaning service, etc.

We want to design a splash page that tourists will initially go to when they want to choose a service that we offer.

INSTRUCTIONS:
This page must speak to tourists in Phuket, Thailand. Should be Thailand Island theme.

GO 4 IT (logo)

CONTENT:

ALL YOU NEED WHILE TRAVELING IN PHUKET, THAILAND

CHOOSE A SERVICE BELOW TO GET STARTED

MOTORBIKE RENTALS
ACTIVITY AND TOUR PACKAGES (COMING SOON)
LAUNDRY PICK UP AND DELIVER SERVICE (COMING SOON)
MAID SERVICE (COMING SOON)
MASSAGE SERVICE TO YOUR ROOM (COMING SOON)
VISA SERVICE (COMING SOON)

Target Market(s)

TOURISTS IN PHUKET THAILAND

Industry/Entity Type

TOURISM

Number of Pages Required

1 page

Requirements
Must have
• We are creating an app that will allow a tourist to request a variety of services on demand. Such as motorbike rentals, in room massage, pick up and laundry delivery service, maid cleaning service, etc. We want to design a splash page that tourists will initially go to when they want to choose a service that we offer. INSTRUCTIONS: This page must speak to tourists in Phuket, Thailand. Should be Thailand Island theme. GO 4 IT (logo) CONTENT: ALL YOU NEED WHILE TRAVELING IN PHUKET, THAILAND CHOOSE A SERVICE BELOW TO GET STARTED MOTORBIKE RENTALS ACTIVITY AND TOUR PACKAGES (COMING SOON) LAUNDRY PICK UP AND DELIVER SERVICE (COMING SOON) MAID SERVICE (COMING SOON) MASSAGE SERVICE TO YOUR ROOM (COMING SOON) VISA SERVICE (COMING SOON)
Nice to have
Should not have

```html
<!DOCTYPE html>
<html lang="en">
<head>
<meta charset="utf-8">
<title>GO 4 IT – Services in Phuket</title>
<link href="https://fonts.googleapis.com/css2?family=Oswald:wght@400;500;600;700&family=Heebo:wght@500;700&display=swap" rel="stylesheet">
<style>
:root{
  --orange:#f07a12;
  --ink:#2b2b2b;
  --white:#ffffff;
  --black:#000000;
  --panel:rgba(236,240,246,0.82);
  --sky-top:#3f7fd6;
  --sky-mid:#a9cdec;
  --sea:#7fd3d0;
  --sand:#efe2cc;
}
*{margin:0;padding:0;box-sizing:border-box}
html,body{width:1134px;height:1200px;overflow:hidden;background:var(--white)}
body{position:relative;font-family:'Heebo',sans-serif;color:var(--ink)}

.site-header{position:absolute;left:0;top:0;width:1134px;height:73px;background:var(--white)}
.brand{position:absolute;left:125px;top:4px;width:150px;text-align:left}
.brand-name{font-family:'Oswald',sans-serif;font-weight:700;font-size:40px;line-height:48px;color:var(--orange);letter-spacing:1px}
.brand-tag{font-family:'Oswald',sans-serif;font-weight:500;font-size:7.5px;color:var(--orange);letter-spacing:.6px;margin-top:-2px;white-space:nowrap}
.main-nav{position:absolute;left:413px;top:29px;display:flex;gap:29px}
.main-nav a,.foot-nav a{font-weight:700;font-size:11.5px;letter-spacing:.5px;color:var(--ink);text-decoration:none}
.call{position:absolute;left:846px;top:18px;display:flex;align-items:center;gap:7px}
.call-icon{width:38px;height:38px;border-radius:50%;background:var(--orange);display:flex;align-items:center;justify-content:center}
.call-label{font-size:13.5px;color:var(--orange);font-weight:500;line-height:16px}
.call-number{font-family:'Oswald',sans-serif;font-weight:500;font-size:20px;color:var(--ink);line-height:24px}

.hero{position:absolute;left:0;top:73px;width:1134px;height:730px;
  background:linear-gradient(180deg,var(--sky-top) 0%,var(--sky-mid) 38%,#d9ecf2 58%,var(--sea) 72%,#cfe8dc 84%,var(--sand) 100%)}
.panel{position:absolute;left:107px;top:106px;width:920px;height:513px;background:var(--panel);box-shadow:0 2px 10px rgba(0,0,0,.15)}
.panel h1{position:absolute;left:0;top:36px;width:100%;text-align:center;font-family:'Oswald',sans-serif;font-weight:600;font-size:30px;color:var(--ink);letter-spacing:.2px}
.panel .lead{position:absolute;left:0;top:83px;width:100%;text-align:center;font-family:'Oswald',sans-serif;font-weight:500;font-size:14px;color:var(--orange)}
.service{position:absolute;top:133px;width:242px}
.service-frame{width:242px;height:265px;background:var(--white);padding:5px;box-shadow:0 1px 4px rgba(0,0,0,.15)}
.service-media{position:relative;width:232px;height:255px;display:flex;flex-direction:column;align-items:center;justify-content:center}
.soon{font-family:'Oswald',sans-serif;font-weight:700;font-size:56px;line-height:62px;color:var(--white);text-align:center;text-shadow:0 2px 4px rgba(0,0,0,.3)}
.service-label{font-family:'Oswald',sans-serif;font-weight:500;font-size:16px;color:var(--ink);text-align:center;margin-top:24px;white-space:nowrap}
.tours .service-media{background:linear-gradient(160deg,#3d5f7a,#6fa7bf 50%,#2f5a6a)}
.bikes .service-media{background:linear-gradient(160deg,#e38a2e,#f0a040 55%,#d7781f)}
.massage .service-media{background:linear-gradient(160deg,#3a2e26,#7a5a48 55%,#4a3a30)}
.bikes .title{font-family:'Oswald',sans-serif;font-weight:600;font-size:16px;color:var(--white);margin-top:32px}
.book{margin-top:22px;width:154px;height:46px;border-radius:23px;background:var(--white);color:var(--orange);font-family:'Oswald',sans-serif;font-weight:500;font-size:17px;display:flex;align-items:center;justify-content:center}
.arrow{position:absolute;top:328px;width:38px;height:38px;border-radius:50%;background:var(--orange);display:flex;align-items:center;justify-content:center}

.site-footer{position:absolute;left:0;top:803px;width:1134px;height:397px;background:var(--black);text-align:center}
.foot-brand{position:absolute;left:0;top:50px;width:100%}
.foot-brand .brand-name{font-size:64px;line-height:76px;letter-spacing:2px}
.foot-brand .brand-tag{font-size:11px;letter-spacing:1.6px;margin-top:0}
.foot-nav{position:absolute;left:0;top:174px;width:100%;display:flex;justify-content:center;gap:29px}
.foot-nav a{color:var(--white)}
.social{position:absolute;left:0;top:207px;width:100%;display:flex;justify-content:center;gap:13px}
.social span{width:28px;height:28px;border-radius:50%;background:var(--white);display:block}
.stores{position:absolute;left:0;top:253px;width:100%;display:flex;justify-content:center;gap:30px}
.store{width:144px;height:42px;border:1px solid #a6a6a6;border-radius:7px;color:var(--white);display:flex;flex-direction:column;justify-content:center;text-align:left;padding-left:18px}
.store small{font-size:8.5px;line-height:10px}
.store b{font-size:18px;line-height:20px;font-weight:500}
.copyright{position:absolute;left:0;top:313px;width:100%;color:var(--white);font-weight:700;font-size:11.5px}
</style>
</head>
<body>
<header class="site-header">
  <div class="brand">
    <div class="brand-name">GO 4 IT</div>
    <div class="brand-tag">WHATEVER BRINGS JOY WHILE IN PHUKET</div>
  </div>
  <nav class="main-nav">
    <a href="#">HOME</a><a href="#">ABOUT US</a><a href="#">SERVICES</a><a href="#">CONTACT US</a>
  </nav>
  <div class="call">
    <div class="call-icon">
      <svg width="16" height="16" viewBox="0 0 24 24"><path fill="#fff" d="M6.6 10.8a15.1 15.1 0 0 0 6.6 6.6l2.2-2.2c.3-.3.7-.4 1-.2 1.1.4 2.3.6 3.6.6.6 0 1 .4 1 1V20c0 .6-.4 1-1 1A17 17 0 0 1 3 4c0-.6.4-1 1-1h3.5c.6 0 1 .4 1 1 0 1.3.2 2.5.6 3.6.1.3 0 .7-.2 1z"/></svg>
    </div>
    <div>
      <div class="call-label">Call Us Today</div>
      <div class="call-number">123 555 0199</div>
    </div>
  </div>
</header>

<section class="hero" role="img" aria-label="Phuket island beach with limestone cliffs, turquoise sea and a longtail boat">
  <div class="panel">
    <h1>ALL YOU NEED WHILE TRAVELING IN PHUKET, THAILAND</h1>
    <p class="lead">CHOOSE A SERVICE BELOW TO GET STARTED</p>

    <article class="service tours" style="left:68px">
      <div class="service-frame">
        <div class="service-media" role="img" aria-label="Collage of tropical beach, palm trees and bungalows for tour packages">
          <div class="soon">COMING<br>SOON</div>
        </div>
      </div>
      <div class="service-label">ACTIVITY AND TOUR PACKAGES</div>
    </article>

    <article class="service bikes" style="left:339px">
      <div class="service-frame">
        <div class="service-media" role="img" aria-label="Family riding bikes through green countryside with orange tint">
          <div class="title">MOTORBIKE RENTALS</div>
          <div class="book">BOOK NOW</div>
        </div>
      </div>
    </article>

    <article class="service massage" style="left:611px">
      <div class="service-frame">
        <div class="service-media" role="img" aria-label="Relaxing in-room massage scene with towels">
          <div class="soon">COMING<br>SOON</div>
        </div>
      </div>
      <div class="service-label">MASSAGE SERVICE TO YOUR ROOM</div>
    </article>
  </div>
  <div class="arrow" style="left:87px"><svg width="12" height="12" viewBox="0 0 12 12"><path d="M8 1 3 6l5 5" stroke="#fff" stroke-width="2" fill="none"/></svg></div>
  <div class="arrow" style="left:1007px"><svg width="12" height="12" viewBox="0 0 12 12"><path d="M4 1l5 5-5 5" stroke="#fff" stroke-width="2" fill="none"/></svg></div>
</section>

<footer class="site-footer">
  <div class="foot-brand">
    <div class="brand-name">GO 4 IT</div>
    <div class="brand-tag">WHATEVER BRINGS JOY WHILE IN PHUKET</div>
  </div>
  <nav class="foot-nav">
    <a href="#">HOME</a><a href="#">ABOUT US</a><a href="#">SERVICES</a><a href="#">CONTACT US</a>
  </nav>
  <div class="social" aria-label="Social links"><span></span><span></span><span></span><span></span></div>
  <div class="stores">
    <div class="store"><small>Download on the</small><b>App Market</b></div>
    <div class="store"><small>GET IT ON</small><b>Play Shelf</b></div>
  </div>
  <p class="copyright">© Copyright 2021 &nbsp;Go 4 It &nbsp; | &nbsp; All Rights Reserved</p>
</footer>
</body>
</html>
```